Innovative IT Service Provider seeks engaging overview presentation to capture new business

*Please see attached Creative Brief for full details*

Overall Goals
The goal of this presentation is to provide new, prospective clients with an introduction to Harborline Systems, the services we provide, and what makes us a unique and superior choice for their IT Services. The deck should be able to clearly relay this information while clients review it on their own, without further explanation from a company representative.

Design Goals
We are looking for a professional, modern, streamlined, sleek design that reflects our status as a leader in information technology and innovation.

Company Overview
As an IT Managed Service Provider, companies choose to outsource some or all of their internal IT functions to us to take advantage of our many areas of expertise and so they can focus on their core business, whatever industry they may be in. We also specialize in IT Cyber Security and Consulting, always providing our clients with thought leadership and insight into the latest IT innovations. We ultimately find ways to deliver value to our clients through our various IT solutions.

```html
<!DOCTYPE html>
<html lang="en">
<head>
<meta charset="utf-8">
<title>Harborline Systems – Service Introduction</title>
<link href="https://fonts.googleapis.com/css2?family=IBM+Plex+Sans:wght@300;400;500;600;700&display=swap" rel="stylesheet">
<style>
:root{
  --canvas:#c4c5c7;
  --navy:#1b3766;
  --navy-deep:#152c55;
  --blue:#5b8ccc;
  --blue-line:#d9e4f3;
  --bar-blue:#3a8ccf;
  --bar-light:#a9d6ef;
  --red:#b8262d;
  --ink:#2b3340;
  --muted:#6b7380;
  --white:#ffffff;
  --grid:#e6e9ee;
}
*{box-sizing:border-box;margin:0;padding:0}
html,body{width:1200px;height:3810px;overflow:hidden}
body{background:var(--canvas);font-family:"IBM Plex Sans",Arial,sans-serif;color:var(--ink);position:relative}
.slide{position:absolute;left:99px;width:1001px;height:563px;background:var(--white);overflow:hidden}
.brand{position:absolute;left:14px;top:16px;display:flex;align-items:center;gap:8px;color:var(--navy);font-weight:600;font-size:13px;line-height:1.1;letter-spacing:.6px;text-transform:uppercase}
.brand-mark{width:26px;height:26px;background:var(--navy);flex:none}
.header-rule{position:absolute;left:0;right:0;top:70px;height:2px;background:var(--navy)}

/* slide 1 */
.s-cover{top:93px}
.cover-art{position:absolute;inset:0;background:radial-gradient(ellipse at 60% 62%,#45c6e6 0%,#1a6ec0 28%,#0d3f93 55%,#082a6e 100%)}
.s-cover .brand{left:50%;top:50px;transform:translateX(-50%);color:var(--white);font-size:14px}
.s-cover .brand-mark{background:var(--white);width:30px;height:30px}
.cover-title{position:absolute;left:0;right:0;top:412px;text-align:center;color:var(--white);font-size:46px;font-weight:700}

/* slide 2 */
.s-outline{top:704px}
.outline-head{position:absolute;left:0;right:0;top:0;height:64px;background:var(--white)}
.outline-head h2{position:absolute;right:28px;top:8px;font-size:37px;font-weight:400;color:var(--navy)}
.outline-body{position:absolute;left:0;right:0;top:64px;bottom:0;background:var(--blue)}
.outline-list{list-style:none}
.outline-list li{position:absolute;left:73px;transform:translateY(-50%);color:var(--white);font-size:24px;font-weight:300;white-space:nowrap}
.outline-list span{margin-right:16px}
.outline-rule{position:absolute;left:31px;width:916px;height:1.5px;background:var(--blue-line)}

/* slide 3 */
.s-why{top:1314px}
.why-title{position:absolute;left:0;right:0;top:113px;text-align:center;font-size:37px;font-weight:700;color:var(--navy)}
.why-sub{position:absolute;left:0;right:0;top:168px;text-align:center;font-size:23px;font-weight:400;color:var(--ink)}
.dash{position:absolute;border:2.5px solid var(--navy);background:var(--white)}
.dash svg{width:100%;height:100%;display:block}
.pillars{position:absolute;left:0;right:0;top:459px;height:104px;background:var(--navy);display:flex}
.pillars div{flex:1;display:flex;align-items:center;justify-content:center;color:var(--white);font-size:20px;border-left:1px solid #4e6a98}
.pillars div:first-child{border-left:none}

/* slide 4 */
.s-data{top:1924px}
.data-title{position:absolute;left:45px;top:195px;font-size:37px;font-weight:700;color:var(--navy)}
.data-sub{position:absolute;left:45px;top:250px;font-size:25px;color:var(--navy)}
.data-copy{position:absolute;left:45px;top:306px;width:230px;font-size:18px;line-height:1.25;color:var(--navy)}

/* slide 5 */
.s-trend{top:2535px}
.trend-title{position:absolute;left:36px;top:120px;font-size:25px;font-weight:700;color:var(--navy)}
.trend-sub{position:absolute;left:36px;top:164px;font-size:12px;color:var(--muted)}
.trend-divider{position:absolute;left:579px;top:72px;width:1.5px;height:105px;background:var(--navy)}
.results-pill{position:absolute;left:634px;top:104px;width:100px;height:60px;border-radius:10px;background:var(--navy);color:var(--white);font-weight:600;font-size:13px;display:flex;align-items:center;justify-content:center}
.results-list{position:absolute;left:758px;top:95px;list-style:none;font-size:12.5px;color:var(--navy);line-height:25px}
.chart-card{position:absolute;left:37px;top:228px;width:542px;height:284px;border:1.5px solid #cfd4db;border-radius:4px;background:var(--white)}
.chart-card h3{position:absolute;left:0;width:390px;top:8px;text-align:center;font-size:14px;font-weight:400;color:var(--ink)}
.bars{position:absolute;left:0;top:34px}
.bar-row{position:absolute;left:0;height:14px;width:400px;font-size:10.5px}
.bar-row .lbl{position:absolute;left:0;width:150px;text-align:right;top:0;line-height:14px;color:var(--ink)}
.bar-track{position:absolute;left:158px;width:237px;height:14px;display:flex}
.bar-track i{display:block;height:100%;font-style:normal;color:var(--white);font-size:10px;line-height:14px;text-align:center}
.seg-esc{background:#1f2a63}
.seg-queue{background:#e26a6a}
.seg-cancel{background:var(--bar-light)}
.seg-res{background:var(--bar-blue)}
.seg-sd{background:#c0392b}
.axis-y{position:absolute;left:18px;top:152px;transform:rotate(-90deg);transform-origin:left top;font-size:11px;color:var(--ink)}
.axis-ticks{position:absolute;left:158px;top:243px;width:237px;font-size:10px;color:var(--muted)}
.axis-ticks span{position:absolute;transform:translateX(-50%)}
.axis-title{position:absolute;left:158px;width:237px;top:258px;text-align:center;font-size:11.5px}
.legend{position:absolute;left:401px;top:32px;font-size:11px;line-height:18px;color:var(--ink);list-style:none}
.legend li{display:flex;align-items:center;gap:4px}
.legend li:first-child{font-weight:600}
.legend b{width:8px;height:8px;border-radius:50%;display:inline-block}
.legend-scroll{position:absolute;left:398px;top:34px;width:4px;height:180px;background:#d6d9de}
.bullets{position:absolute;left:617px;top:247px;width:340px;list-style:none;font-size:15.5px;line-height:25px;color:var(--navy)}
.bullets li{position:relative;padding-left:30px;margin-bottom:29px}
.bullets li::before{content:"";position:absolute;left:0;top:8px;width:12px;height:12px;border-radius:50%;background:var(--red)}

/* slide 6 */
.s-staff{top:3145px}
.s-staff .header-rule{top:67px}
.staff-title{position:absolute;left:204px;top:6px;font-size:25px;font-weight:700;color:var(--navy)}
.staff-sub{position:absolute;left:204px;top:42px;font-size:12px;color:var(--muted)}
.binary-field{position:absolute;left:0;right:0;top:300px;bottom:0;background:linear-gradient(180deg,rgba(255,255,255,0) 0%,#e9ecf1 55%,#d3d8e0 100%)}
.report{position:absolute;left:115px;top:104px;width:785px;height:422px;background:var(--white);box-shadow:0 0 10px rgba(0,0,0,.06)}
.filter{position:absolute;left:7px;top:5px;width:168px;font-size:8px;color:var(--ink)}
.filter .dates{display:flex;gap:16px;margin-top:4px}
.filter .dates span{border:1px solid #c9ced6;padding:1px 4px}
.mini-table{position:absolute;left:7px;top:111px;width:168px;font-size:8px;border-collapse:collapse}
.mini-table caption{background:var(--navy);color:var(--white);font-size:8.5px;padding:2px;text-align:center}
.mini-table th{text-align:left;font-weight:500;border-bottom:1px solid #999;padding:1px 3px}
.mini-table td{padding:0 3px;line-height:10.5px}
.mini-table td:last-child{text-align:right}
.mini-table tr.total td{font-weight:700;border-top:1px solid #999}
.line-chart{position:absolute;left:202px;width:565px}
.heat{position:absolute;left:7px;top:279px;width:748px;border-collapse:collapse;font-size:7.2px}
.heat caption{background:var(--navy);color:var(--white);font-size:8.5px;padding:2px}
.heat th{font-weight:500;text-align:left;padding:1px 2px;border-bottom:1px solid #999}
.heat td{padding:0 2px;line-height:10.5px;text-align:right}
.heat td:first-child{text-align:left}
.heat td.w{background:#f2c9c4}
.heat td.h{background:#e59a92}
.heat tr.total td{font-weight:700;border-top:1px solid #999}
</style>
</head>
<body>

<!-- Cover -->
<section class="slide s-cover">
  <div class="cover-art" role="img" aria-label="Blue digital wave of glowing particles"></div>
  <div class="brand"><span class="brand-mark"></span><span class="brand-name">Harborline<br>Systems</span></div>
  <h1 class="cover-title">Service Introduction</h1>
</section>

<!-- Outline -->
<section class="slide s-outline">
  <div class="outline-head">
    <div class="brand"><span class="brand-mark"></span><span class="brand-name">Harborline<br>Systems</span></div>
    <h2>Outline</h2>
  </div>
  <div class="outline-body">
    <ol class="outline-list">
      <li style="top:94px"><span>01.</span>Why HS</li>
      <li style="top:190px"><span>02.</span>ITSM Transformation &amp; Maturity</li>
      <li style="top:287px"><span>03.</span>Continuous Improvement Framework</li>
      <li style="top:383px"><span>04.</span>HS Service Towers Overview</li>
    </ol>
    <div class="outline-rule" style="top:136px"></div>
    <div class="outline-rule" style="top:240px"></div>
    <div class="outline-rule" style="top:336px"></div>
  </div>
</section>

<!-- Why HS: measured -->
<section class="slide s-why">
  <div class="brand"><span class="brand-mark"></span><span class="brand-name">Harborline<br>Systems</span></div>
  <div class="header-rule"></div>
  <h2 class="why-title">Why HS?</h2>
  <p class="why-sub">Measured, Managed &amp; Mature</p>

  <div class="dash" style="left:15px;top:250px;width:326px;height:165px">
    <svg viewBox="0 0 326 165" preserveAspectRatio="none">
      <rect x="0" y="0" width="326" height="9" fill="#1b3766"/>
      <text x="163" y="7" font-size="6" fill="#fff" text-anchor="middle">Calls</text>
      <path d="M14 70 A22 22 0 0 1 58 70" fill="none" stroke="#e3e6ea" stroke-width="8"/>
      <text x="36" y="68" font-size="7" text-anchor="middle" fill="#555">2.00%</text>
      <path d="M78 70 A22 22 0 0 1 122 70" fill="none" stroke="#1b3766" stroke-width="8"/>
      <text x="100" y="68" font-size="7" text-anchor="middle" fill="#555">99%</text>
      <text x="12" y="32" font-size="4" fill="#666">Abandon Rate</text>
      <text x="80" y="32" font-size="4" fill="#666">Answer Rate</text>
      <g fill="#c9d5e7"><rect x="150" y="40" width="60" height="4"/><rect x="150" y="48" width="40" height="4"/><rect x="150" y="56" width="70" height="4"/><rect x="150" y="64" width="50" height="4"/></g>
      <g fill="#eef1f5"><rect x="215" y="40" width="90" height="4"/><rect x="215" y="48" width="90" height="4"/><rect x="215" y="56" width="90" height="4"/></g>
      <text x="20" y="140" font-size="11" fill="#1b3766">15</text>
      <text x="115" y="140" font-size="11" fill="#1b3766">2.00%</text>
      <text x="230" y="140" font-size="11" fill="#1b3766">140</text>
      <g fill="#dde4ee"><rect x="55" y="110" width="40" height="30"/><rect x="175" y="110" width="40" height="30"/><rect x="268" y="110" width="45" height="30"/></g>
    </svg>
  </div>
  <div class="dash" style="left:359px;top:250px;width:309px;height:165px">
    <svg viewBox="0 0 309 165" preserveAspectRatio="none">
      <rect x="6" y="6" width="48" height="10" fill="#1b3766"/>
      <text x="30" y="13" font-size="5" fill="#fff" text-anchor="middle">Survey Results</text>
      <text x="90" y="32" font-size="10" fill="#1b3766">4.65</text>
      <text x="150" y="32" font-size="10" fill="#1b3766">33</text>
      <g fill="#c9d9ee"><rect x="200" y="6" width="100" height="6"/><rect x="200" y="14" width="100" height="6"/><rect x="200" y="22" width="100" height="6"/></g>
      <g fill="#9fbde0"><rect x="40" y="58" width="260" height="5"/><rect x="40" y="66" width="260" height="5"/></g>
      <rect x="0" y="106" width="309" height="9" fill="#1b3766"/>
      <text x="154" y="113" font-size="6" fill="#fff" text-anchor="middle">Handling Accuracy</text>
      <text x="14" y="150" font-size="11" fill="#1b3766">99.50%</text>
      <g fill="#e7ebf1"><rect x="95" y="122" width="90" height="36"/><rect x="195" y="122" width="100" height="36"/></g>
    </svg>
  </div>
  <div class="dash" style="left:687px;top:250px;width:303px;height:165px">
    <svg viewBox="0 0 303 165" preserveAspectRatio="none">
      <g fill="#b9c7dc"><rect x="25" y="35" width="8" height="60"/></g>
      <rect x="34" y="35" width="8" height="55" fill="#4a6fa5"/>
      <g fill="#eef1f5"><rect x="95" y="25" width="75" height="70"/></g>
      <rect x="220" y="48" width="30" height="6" fill="#1b3766"/>
      <circle cx="40" cy="130" r="22" fill="#1b3766"/>
      <path d="M40 130 L40 108 A22 22 0 0 1 62 130 Z" fill="#c0392b"/>
      <path d="M40 130 L62 130 A22 22 0 0 1 45 151 Z" fill="#5b8ccc"/>
      <circle cx="190" cy="130" r="22" fill="#1b3766"/>
      <path d="M190 130 L190 108 A22 22 0 0 1 211 124 Z" fill="#c0392b"/>
      <path d="M190 130 L168 130 A22 22 0 0 1 190 108 Z" fill="#8fb2dd"/>
      <text x="75" y="105" font-size="4" fill="#666">Top Categories</text>
    </svg>
  </div>

  <div class="pillars">
    <div>Business Analytics</div>
    <div>Trend Analysis</div>
    <div>Continuous Improvement</div>
  </div>
</section>

<!-- Why HS: data driven -->
<section class="slide s-data">
  <div class="brand"><span class="brand-mark"></span><span class="brand-name">Harborline<br>Systems</span></div>
  <div class="header-rule"></div>
  <h2 class="data-title">Why HS?</h2>
  <p class="data-sub">Data Driven Excellence</p>
  <p class="data-copy">Mature dashboards, trend analysis, and thought leadership to drive improvements</p>

  <div class="dash" style="left:355px;top:128px;width:268px;height:167px">
    <svg viewBox="0 0 268 167" preserveAspectRatio="none">
      <g font-size="5" fill="#1b3766">
        <text x="6" y="9">Priority 1 – Response SLA by Month</text>
        <text x="6" y="64">Priority 2 – Response SLA by Month</text>
        <text x="6" y="118">Priority 3 – Response SLA by Month</text>
      </g>
      <g fill="none" stroke="#1b3766" stroke-width="1.2">
        <polyline points="20,26 45,28 70,24 95,30 120,25 145,27 170,22 195,29 220,26 255,24"/>
        <polyline points="20,82 45,80 70,84 95,79 120,83 145,81 170,98 195,82 220,80 255,83"/>
        <polyline points="20,136 45,138 70,134 95,137 120,135 145,139 170,134 195,136 220,138 255,135"/>
      </g>
      <g stroke="#e0e4ea"><line x1="0" y1="55" x2="268" y2="55"/><line x1="0" y1="110" x2="268" y2="110"/></g>
    </svg>
  </div>
  <div class="dash" style="left:640px;top:128px;width:334px;height:167px">
    <svg viewBox="0 0 334 167" preserveAspectRatio="none">
      <rect x="0" y="0" width="334" height="9" fill="#1b3766"/>
      <text x="167" y="7" font-size="6" fill="#fff" text-anchor="middle">Calls</text>
      <path d="M14 72 A22 22 0 0 1 58 72" fill="none" stroke="#e3e6ea" stroke-width="8"/>
      <text x="36" y="70" font-size="7" text-anchor="middle" fill="#555">2.00%</text>
      <path d="M78 72 A22 22 0 0 1 122 72" fill="none" stroke="#1b3766" stroke-width="8"/>
      <text x="100" y="70" font-size="7" text-anchor="middle" fill="#555">99%</text>
      <g fill="#c9d5e7"><rect x="150" y="40" width="60" height="4"/><rect x="150" y="48" width="40" height="4"/><rect x="150" y="56" width="70" height="4"/></g>
      <text x="20" y="142" font-size="11" fill="#1b3766">15</text>
      <text x="118" y="142" font-size="11" fill="#1b3766">2.00%</text>
      <text x="235" y="142" font-size="11" fill="#1b3766">140</text>
      <g fill="#dde4ee"><rect x="55" y="112" width="40" height="30"/><rect x="178" y="112" width="40" height="30"/><rect x="275" y="112" width="45" height="30"/></g>
    </svg>
  </div>
  <div class="dash" style="left:355px;top:319px;width:311px;height:166px">
    <svg viewBox="0 0 311 166" preserveAspectRatio="none">
      <rect x="6" y="6" width="48" height="10" fill="#1b3766"/>
      <text x="30" y="13" font-size="5" fill="#fff" text-anchor="middle">Survey Results</text>
      <text x="90" y="32" font-size="10" fill="#1b3766">4.65</text>
      <text x="150" y="32" font-size="10" fill="#1b3766">33</text>
      <g fill="#c9d9ee"><rect x="200" y="6" width="100" height="6"/><rect x="200" y="14" width="100" height="6"/></g>
      <g fill="#9fbde0"><rect x="40" y="58" width="260" height="5"/><rect x="40" y="66" width="260" height="5"/></g>
      <rect x="0" y="104" width="311" height="9" fill="#1b3766"/>
      <text x="155" y="111" font-size="6" fill="#fff" text-anchor="middle">Handling Accuracy</text>
      <text x="14" y="150" font-size="11" fill="#1b3766">99.50%</text>
      <g fill="#e7ebf1"><rect x="95" y="120" width="90" height="38"/><rect x="195" y="120" width="100" height="38"/></g>
    </svg>
  </div>
  <div class="dash" style="left:678px;top:319px;width:296px;height:166px">
    <svg viewBox="0 0 296 166" preserveAspectRatio="none">
      <g fill="#9fb3d1"><rect x="15" y="40" width="4" height="20"/><rect x="22" y="36" width="4" height="24"/><rect x="29" y="42" width="4" height="18"/><rect x="36" y="38" width="4" height="22"/><rect x="43" y="40" width="4" height="20"/><rect x="50" y="35" width="4" height="25"/></g>
      <rect x="100" y="32" width="24" height="38" fill="#111"/>
      <g fill="#5b8ccc"><rect x="220" y="36" width="40" height="4"/><rect x="220" y="44" width="30" height="4"/><rect x="220" y="52" width="45" height="4"/></g>
      <circle cx="50" cy="128" r="22" fill="#1b3766"/>
      <path d="M50 128 L50 106 A22 22 0 0 1 70 120 Z" fill="#8fb2dd"/>
      <circle cx="170" cy="128" r="22" fill="#1b3766"/>
      <path d="M170 128 L170 106 A22 22 0 0 1 191 122 Z" fill="#c0392b"/>
      <path d="M170 128 L148 128 A22 22 0 0 1 170 106 Z" fill="#5b8ccc"/>
    </svg>
  </div>
</section>

<!-- Service desk trends -->
<section class="slide s-trend">
  <div class="brand"><span class="brand-mark"></span><span class="brand-name">Harborline<br>Systems</span></div>
  <div class="header-rule"></div>
  <h2 class="trend-title">Service Desk Trends Example</h2>
  <p class="trend-sub">Example - Driving Up Service Desk Resolution due to Continuous Improvement</p>
  <div class="trend-divider"></div>
  <div class="results-pill">RESULTS</div>
  <ul class="results-list">
    <li>Increased First-Call Resolution</li>
    <li>Reduced Mean Time to Resolution</li>
    <li>Improved Shift Left</li>
  </ul>

  <div class="chart-card">
    <h3>Service Desk Status by Opened Month</h3>
    <div class="axis-y">YearMonth</div>
    <div class="bars">
      <div class="bar-row" style="top:0"><span class="lbl">April 2022</span><div class="bar-track"><i class="seg-esc" style="width:33.46%">33.46%</i><i class="seg-cancel" style="width:5.5%"></i><i class="seg-res" style="width:60.37%">60.37%</i><i class="seg-sd" style="width:.67%"></i></div></div>
      <div class="bar-row" style="top:20px"><span class="lbl">May 2022</span><div class="bar-track"><i class="seg-esc" style="width:32.06%">32.06%</i><i class="seg-cancel" style="width:4.3%"></i><i class="seg-res" style="width:63.19%">63.19%</i><i class="seg-sd" style="width:.45%"></i></div></div>
      <div class="bar-row" style="top:40px"><span class="lbl">June 2022</span><div class="bar-track"><i class="seg-esc" style="width:37.60%">37.60%</i><i class="seg-cancel" style="width:3.4%"></i><i class="seg-res" style="width:58.51%">58.51%</i><i class="seg-sd" style="width:.49%"></i></div></div>
      <div class="bar-row" style="top:60px"><span class="lbl">July 2022</span><div class="bar-track"><i class="seg-esc" style="width:38.80%">38.80%</i><i class="seg-cancel" style="width:3.3%"></i><i class="seg-res" style="width:57.40%">57.40%</i><i class="seg-sd" style="width:.5%"></i></div></div>
      <div class="bar-row" style="top:80px"><span class="lbl">August 2022</span><div class="bar-track"><i class="seg-esc" style="width:38.08%">38.08%</i><i class="seg-cancel" style="width:2.5%"></i><i class="seg-res" style="width:58.91%">58.91%</i><i class="seg-sd" style="width:.51%"></i></div></div>
      <div class="bar-row" style="top:100px"><span class="lbl">September 2022</span><div class="bar-track"><i class="seg-esc" style="width:36.08%">36.08%</i><i class="seg-cancel" style="width:1.9%"></i><i class="seg-res" style="width:61.55%">61.55%</i><i class="seg-sd" style="width:.47%"></i></div></div>
      <div class="bar-row" style="top:120px"><span class="lbl">October 2022</span><div class="bar-track"><i class="seg-esc" style="width:35.29%">35.29%</i><i class="seg-cancel" style="width:2.2%"></i><i class="seg-res" style="width:62.06%">62.06%</i><i class="seg-sd" style="width:.45%"></i></div></div>
      <div class="bar-row" style="top:140px"><span class="lbl">November 2022</span><div class="bar-track"><i class="seg-esc" style="width:32.76%">32.76%</i><i class="seg-cancel" style="width:2%"></i><i class="seg-res" style="width:61.87%">61.87%</i><i class="seg-sd" style="width:3.37%"></i></div></div>
      <div class="bar-row" style="top:160px"><span class="lbl">December 2022</span><div class="bar-track"><i class="seg-esc" style="width:25.64%">25.64%</i><i class="seg-cancel" style="width:1.6%"></i><i class="seg-res" style="width:72.34%">72.34%</i><i class="seg-sd" style="width:.42%"></i></div></div>
      <div class="bar-row" style="top:180px"><span class="lbl">January 2023</span><div class="bar-track"><i class="seg-esc" style="width:25.73%">25.73%</i><i class="seg-queue" style="width:1.2%"></i><i class="seg-cancel" style="width:1.6%"></i><i class="seg-res" style="width:71.04%">71.04%</i><i class="seg-sd" style="width:.43%"></i></div></div>
    </div>
    <div class="legend-scroll"></div>
    <ul class="legend">
      <li>SD_Status</li>
      <li><b style="background:#1f2a63"></b>Escalated</li>
      <li><b style="background:#e26a6a"></b>In Service Desk Queue</li>
      <li><b style="background:var(--bar-light)"></b>Incident Canceled</li>
      <li><b style="background:var(--bar-blue)"></b>Resolved by Service Desk</li>
      <li><b style="background:#c0392b"></b>Resolved in Service Des...</li>
    </ul>
    <div class="axis-ticks"><span style="left:0">0%</span><span style="left:50%">50%</span><span style="left:100%">100%</span></div>
    <div class="axis-title">Count of number</div>
  </div>

  <ul class="bullets">
    <li>Service Desk Resolution and customer experience is highly managed from arrival of ticket to resolution</li>
    <li>Client Management team works with customer to drive CSI across the HS delivery organization</li>
    <li>Improved Knowledge, Access, Training and Expertise yields results.</li>
  </ul>
</section>

<!-- Data driven staffing -->
<section class="slide s-staff">
  <div class="brand"><span class="brand-mark"></span><span class="brand-name">Harborline<br>Systems</span></div>
  <h2 class="staff-title">Data Driven Excellence</h2>
  <p class="staff-sub">Mature call arrival analysis to drive appropriate staffing to meet demand</p>
  <div class="header-rule"></div>
  <div class="binary-field" role="img" aria-label="Faint binary digit pattern fading in from the bottom"></div>

  <div class="report">
    <div class="filter">Date
      <div class="dates"><span>7/1/2022</span><span>7/27/2023</span></div>
      <svg width="160" height="14" viewBox="0 0 160 14"><line x1="42" y1="7" x2="152" y2="7" stroke="#555" stroke-width="2"/><circle cx="42" cy="7" r="5" fill="#fff" stroke="#555"/><circle cx="152" cy="7" r="5" fill="#fff" stroke="#555"/></svg>
    </div>
    <table class="mini-table">
      <caption>Average Number of Long Abandons by Weekday</caption>
      <tr><th>WeekdayName</th><th>Avg Long Abandons per day</th></tr>
      <tr><td>Sunday</td><td>2.80</td></tr>
      <tr><td>Monday</td><td>5.82</td></tr>
      <tr><td>Tuesday</td><td>5.58</td></tr>
      <tr><td>Wednesday</td><td>7.15</td></tr>
      <tr><td>Thursday</td><td>3.14</td></tr>
      <tr><td>Friday</td><td>3.45</td></tr>
      <tr><td>Saturday</td><td>2.64</td></tr>
      <tr class="total"><td>Total</td><td>4.57</td></tr>
    </table>

    <svg class="line-chart" style="top:2px" height="120" viewBox="0 0 565 120">
      <text x="0" y="9" font-size="9" fill="#333">Avg Contacts by Weekday (Answered and Abandons)</text>
      <g font-size="7" fill="#666"><text x="10" y="24">200</text><text x="10" y="48">150</text><text x="10" y="72">100</text><text x="10" y="96">50</text><text x="14" y="114">0</text></g>
      <polyline fill="none" stroke="#1b3766" stroke-width="1.5" points="60,87 135,28 210,28 287,21 362,36 438,40 513,84"/>
      <g font-size="7" fill="#333" text-anchor="middle"><text x="60" y="82">51</text><text x="135" y="24">180</text><text x="210" y="24">181</text><text x="287" y="17">194</text><text x="362" y="32">163</text><text x="438" y="36">147</text><text x="513" y="80">59</text></g>
      <g font-size="7" fill="#666" text-anchor="middle"><text x="60" y="120">Sunday</text><text x="135" y="120">Monday</text><text x="210" y="120">Tuesday</text><text x="287" y="120">Wednesday</text><text x="362" y="120">Thursday</text><text x="438" y="120">Friday</text><text x="513" y="120">Saturday</text></g>
    </svg>
    <svg class="line-chart" style="top:140px" height="130" viewBox="0 0 565 130">
      <text x="0" y="9" font-size="9" fill="#333">Avg Contacts by Hour Of Day (Answered and Abandons)</text>
      <g font-size="7" fill="#666"><text x="14" y="48">10</text><text x="18" y="100">0</text></g>
      <polyline fill="none" stroke="#1b3766" stroke-width="1.5" points="30,86 52,88 74,88 96,88 118,88 140,87 162,84 184,72 206,56 228,44 250,46 272,47 294,48 316,49 338,48 360,50 382,54 404,67 426,76 448,80 470,83 492,85 514,86 536,88"/>
      <g font-size="7" fill="#333" text-anchor="middle"><text x="30" y="82">3</text><text x="96" y="84">2</text><text x="228" y="40">12</text><text x="272" y="43">11</text><text x="316" y="45">11</text><text x="404" y="63">7</text><text x="448" y="76">4</text><text x="492" y="81">3</text><text x="536" y="84">2</text></g>
      <g font-size="7" fill="#666" text-anchor="middle"><text x="30" y="104">0</text><text x="140" y="104">5</text><text x="250" y="104">10</text><text x="360" y="104">15</text><text x="470" y="104">20</text><text x="280" y="114">HourOfDay</text></g>
    </svg>

    <table class="heat">
      <caption>Average Number of Contacts by Weekday and Hour of Day (Answered, Long Abandons and Short Abandons)</caption>
      <tr><th>WeekdayName</th><th>0</th><th>1</th><th>2</th><th>3</th><th>4</th><th>5</th><th>6</th><th>7</th><th>8</th><th>9</th><th>10</th><th>11</th><th>12</th><th>13</th><th>14</th><th>15</th><th>16</th><th>17</th><th>18</th><th>19</th><th>20</th><th>21</th><th>22</th><th>23</th><th>Total</th></tr>
      <tr><td>Sunday</td><td>1.84</td><td>2.10</td><td>1.64</td><td>1.88</td><td>1.44</td><td>1.92</td><td>2.58</td><td>2.83</td><td>3.08</td><td>2.81</td><td>3.16</td><td>3.67</td><td>3.60</td><td>3.37</td><td>2.63</td><td>3.02</td><td>3.00</td><td>2.52</td><td>2.43</td><td>3.12</td><td>2.74</td><td>2.45</td><td>2.50</td><td>2.56</td><td>50.75</td></tr>
      <tr><td>Monday</td><td>2.72</td><td>2.37</td><td>3.08</td><td>2.35</td><td>2.36</td><td>2.56</td><td>3.63</td><td class="w">5.83</td><td class="h">12.82</td><td class="h">14.43</td><td class="h">15.78</td><td class="h">15.88</td><td class="h">13.70</td><td class="h">14.58</td><td class="h">14.55</td><td class="h">13.77</td><td class="h">12.89</td><td class="w">8.71</td><td class="w">6.38</td><td>4.73</td><td>4.24</td><td>3.02</td><td>2.67</td><td>2.12</td><td>180.13</td></tr>
      <tr><td>Tuesday</td><td>2.67</td><td>2.10</td><td>2.32</td><td>2.21</td><td>2.02</td><td>2.30</td><td>2.96</td><td class="w">6.69</td><td class="h">13.13</td><td class="h">15.80</td><td class="h">17.02</td><td class="h">14.66</td><td class="h">14.48</td><td class="h">14.70</td><td class="h">14.03</td><td class="h">14.86</td><td class="h">12.25</td><td class="w">9.07</td><td class="w">5.13</td><td>4.80</td><td>4.13</td><td>3.15</td><td>2.42</td><td>2.31</td><td>181.04</td></tr>
      <tr><td>Wednesday</td><td>2.39</td><td>1.79</td><td>1.81</td><td>2.03</td><td>2.00</td><td>2.32</td><td>3.22</td><td class="w">7.64</td><td class="h">14.61</td><td class="h">16.45</td><td class="h">16.73</td><td class="h">16.07</td><td class="h">16.00</td><td class="h">14.41</td><td class="h">15.82</td><td class="h">15.71</td><td class="h">13.27</td><td class="h">10.07</td><td class="w">7.46</td><td class="w">5.87</td><td>4.27</td><td>3.70</td><td>3.15</td><td>2.70</td><td>194.32</td></tr>
      <tr><td>Thursday</td><td>2.42</td><td>2.67</td><td>2.34</td><td>2.59</td><td>2.43</td><td>2.65</td><td>3.08</td><td class="w">5.32</td><td class="h">11.81</td><td class="h">14.02</td><td class="h">14.91</td><td class="h">15.09</td><td class="h">13.80</td><td class="h">13.70</td><td class="h">12.70</td><td class="h">12.31</td><td class="h">10.70</td><td class="w">6.48</td><td class="w">5.02</td><td>3.98</td><td>3.08</td><td>2.66</td><td>2.59</td><td>2.48</td><td>162.94</td></tr>
      <tr><td>Friday</td><td>3.21</td><td>2.90</td><td>2.20</td><td>2.50</td><td>2.33</td><td>2.13</td><td>2.78</td><td>4.89</td><td class="w">9.02</td><td class="h">12.29</td><td class="h">13.47</td><td class="h">13.48</td><td class="h">12.00</td><td class="h">11.95</td><td class="h">12.61</td><td class="h">10.80</td><td class="w">9.57</td><td class="w">5.91</td><td>3.61</td><td>3.78</td><td>3.44</td><td>2.72</td><td>2.78</td><td>2.24</td><td>146.70</td></tr>
      <tr><td>Saturday</td><td>2.38</td><td>1.96</td><td>2.33</td><td>2.02</td><td>1.83</td><td>1.95</td><td>2.25</td><td>3.02</td><td>3.73</td><td>3.96</td><td>4.81</td><td>5.06</td><td>4.55</td><td>4.09</td><td>3.64</td><td>3.90</td><td>3.00</td><td>2.32</td><td>2.21</td><td>2.00</td><td>2.23</td><td>1.68</td><td>1.91</td><td>1.61</td><td>58.73</td></tr>
      <tr class="total"><td>Total</td><td>2.55</td><td>2.28</td><td>2.30</td><td>2.23</td><td>2.05</td><td>2.25</td><td>2.86</td><td>5.27</td><td>9.93</td><td>13.49</td><td>12.43</td><td>12.18</td><td>11.32</td><td>11.11</td><td>11.27</td><td>10.88</td><td>9.47</td><td>6.57</td><td>4.70</td><td>4.11</td><td>3.49</td><td>2.81</td><td>2.61</td><td>2.32</td><td>139.11</td></tr>
    </table>
  </div>
</section>

</body>
</html>
```